Poster for a 100 y.o. Tennis Tournament

I would like a poster designed to promote our tennis tournament but I'd like to avoid some of the clichés like the shadow of a player serving. Just well styled text would be fine but some clever imagery would be a bonus.
Highlighting the fact our tournament has been running for over 100 years would be nice so a retro design would work. But that doesn't mean a modern design, for example a minimalist approach utilising the lines of a tennis court, wouldn't work.
Updates

Our tennis committee is now in the process of short listing and will provide an update within 48 hours.

Industry/Entity Type

Court

Requirements
Must have
• The poster must contain the following text at a minimum:
"Marbury Tennis Tournament"/"Since 1908"
"9 March - 11 March, 2013" or "9-11 March, 2013", etc
"www.marburytennis.com.au"

The poster must be reproducible in colour and black & white, or at least have an alternate for black & white.

The poster must be usable in both A3 and A4 sizes.
Nice to have
• The poster should contain the following text:
"Championship"
"Handicap"
"Seniors"
"Juniors"
Each above may be optionally succeeded by "Singles & Doubles", e.g. "Championship Singles & Doubles". It would actually be clearer if this additional text was used but would be repetitive, so alternate text "Singles & Doubles in all categories" might also be used. Alternatives for variety (with the first word the focus): "Championship Singles & Doubles", "Handicap Singles & Doubles", "Seniors 35+ & 50+", "Juniors 18&U, 14&U"

Ideally the poster will provision room for four to eight sponsors logos, preferably at the bottom, but failure to do this is not a show stopper.

The following text may also be used:
"Entries close February 24"
"Tollard Plate Weekend"

Attached is a photo of one of the old trophies. Utilisation of the curved style of the "Marbury Tennis Tournament" text would fit in with the history if the tournament.

The ability to reuse elements of the poster in a single page website used to promote the tournament would be an advantage (as it will provide consistency).

If you could have an image of a tennis ball that conveys the same energy as the clock/tyre image in the attached "Under the Glass Moon" poster, that would be cool. Or using split imagery of a wooden racquet and a modern racquet, but with some energy, would also be good. These are just ideas though and by no means essential.

I've also attached a photo of a t-shirt with a poster layout I thought looked good.

Some additional text that can be used:
"Brand new courts"
"Brindle Park, Oakhurst Tce, Marbury"
"Phone 0427 318 642"
"Prizes and Trophies"

```html
<!DOCTYPE html>
<html lang="en">
<head>
<meta charset="utf-8">
<title>Marbury Tennis Tournament</title>
<link rel="stylesheet" href="https://fonts.googleapis.com/css2?family=Graduate&family=Oswald:wght@500;600&display=swap">
<style>
  :root {
    --grass-dark: #2f6e1f;
    --grass: #4a9a30;
    --grass-light: #6cb544;
    --ball-light: #eef25a;
    --ball: #d6e43a;
    --ball-edge: #aac425;
    --title-yellow: #eef04e;
    --ink-green: #1f4a14;
    --white: #ffffff;
  }
  html, body {
    margin: 0;
    padding: 0;
    overflow: hidden;
    background: var(--grass-dark);
  }
  .poster {
    position: relative;
    width: 849px;
    height: 1200px;
    overflow: hidden;
    background: radial-gradient(ellipse at 50% 30%, var(--grass-light) 0%, var(--grass) 45%, var(--grass-dark) 100%);
    font-family: "Oswald", "Arial Narrow", sans-serif;
    text-align: center;
  }
  .title {
    position: absolute;
    top: 28px;
    left: 0;
    width: 100%;
    margin: 0;
    font-family: "Graduate", serif;
    font-weight: 400;
    font-size: 86px;
    line-height: 96px;
    color: var(--title-yellow);
    text-shadow: 3px 3px 0 var(--ink-green), -1px -1px 0 var(--ink-green), 1px -1px 0 var(--ink-green), -1px 1px 0 var(--ink-green);
    letter-spacing: 1px;
  }
  .centenary-badge {
    position: absolute;
    top: 150px;
    right: 62px;
    width: 64px;
    height: 64px;
  }
  .dates {
    position: absolute;
    top: 252px;
    left: 0;
    width: 100%;
    margin: 0;
    font-weight: 600;
    font-size: 56px;
    line-height: 64px;
    color: var(--white);
    letter-spacing: 1px;
  }
  .entries {
    position: absolute;
    top: 318px;
    left: 0;
    width: 100%;
    margin: 0;
    font-weight: 500;
    font-size: 24px;
    color: var(--white);
    letter-spacing: 1px;
  }
  .website {
    position: absolute;
    top: 418px;
    left: 0;
    width: 100%;
    margin: 0;
    font-weight: 500;
    font-size: 34px;
    color: var(--title-yellow);
    letter-spacing: 1px;
  }
  .ball {
    position: absolute;
    left: -185px;
    top: 520px;
    width: 1220px;
    height: 1220px;
    border-radius: 50%;
    background: radial-gradient(circle at 50% 30%, var(--ball-light) 0%, var(--ball) 45%, var(--ball-edge) 100%);
  }
  .weekend {
    position: absolute;
    top: 580px;
    left: 0;
    width: 100%;
    margin: 0;
    font-weight: 600;
    font-size: 30px;
    color: var(--ink-green);
    letter-spacing: 1px;
  }
  .perks {
    position: absolute;
    top: 630px;
    left: 0;
    width: 100%;
    margin: 0;
    font-weight: 500;
    font-size: 20px;
    line-height: 26px;
    color: var(--ink-green);
    letter-spacing: 1px;
  }
  .category {
    position: absolute;
    width: 440px;
    text-align: center;
    color: var(--ink-green);
  }
  .category-name {
    display: block;
    font-family: "Graduate", serif;
    font-size: 46px;
    line-height: 52px;
  }
  .category-detail {
    display: block;
    font-family: "Graduate", serif;
    font-size: 22px;
    line-height: 30px;
  }
  .championship { left: 40px; top: 820px; }
  .seniors { left: 440px; top: 820px; width: 360px; }
  .handicap { left: 10px; top: 955px; width: 400px; }
  .juniors { left: 440px; top: 955px; width: 360px; }
  .contact {
    position: absolute;
    bottom: 26px;
    left: 0;
    width: 100%;
    margin: 0;
    font-weight: 500;
    font-size: 17px;
    color: var(--ink-green);
    letter-spacing: 1px;
  }
</style>
</head>
<body>
<main class="poster">
  <h1 class="title">MARBURY TENNIS<br>TOURNAMENT</h1>
  <svg class="centenary-badge" viewBox="0 0 64 64" aria-hidden="true">
    <circle cx="32" cy="32" r="30" fill="var(--title-yellow)" stroke="var(--ink-green)" stroke-width="3"/>
  </svg>
  <p class="dates">9 - 11 MARCH 2013</p>
  <p class="entries">ENTRIES CLOSE FEBRUARY 24</p>
  <p class="website">WWW.MARBURYTENNIS.COM.AU</p>

  <div class="ball" role="img" aria-label="Large tennis ball illustration"></div>

  <p class="weekend">TOLLARD PLATE WEEKEND</p>
  <p class="perks">PRIZES AND TROPHIES<br>BRAND NEW COURTS</p>

  <div class="category championship">
    <span class="category-name">CHAMPIONSHIP</span>
    <span class="category-detail">SINGLES &amp; DOUBLES</span>
  </div>
  <div class="category seniors">
    <span class="category-name">SENIORS</span>
    <span class="category-detail">35+ &amp; 50+</span>
  </div>
  <div class="category handicap">
    <span class="category-name">HANDICAP</span>
    <span class="category-detail">SINGLES &amp; DOUBLES</span>
  </div>
  <div class="category juniors">
    <span class="category-name">JUNIORS</span>
    <span class="category-detail">18&amp;U 14&amp;U GREEN BALL</span>
  </div>

  <p class="contact">PHONE 0427 318 642 - BRINDLE PARK, OAKHURST TCE, MARBURY</p>
</main>
</body>
</html>
```